Flyer Design - Spill Management Products - Selling to new clients

I am looking to produce an A4 double sided flyer. It is promoting our spill management products to prospective clients. This flyer is specifically targetting coal mines near where we operate.
I am not sure if I have provided too much text to fit in 2 pages, if so, I can reduce it if needed.
As it is selling to prospective clients, I think it needs to grab their attention. I basically want a bit of text, selling us and our company too them, and then feature a number of products.
If you need more clarification on what we want, please ask.
I would like it designed in InDesign if possible, as we have someone in house that could make changes to it when needed. I also intend to have this professionally printed.
You can view our company here – www.brantoveck.com.au
I have added a word document with details of what is to be included, plus the required images.
Cheers,
Oskar

```html
<!DOCTYPE html>
<html lang="en">
<head>
<meta charset="utf-8">
<title>Brantoveck Flyer</title>
<link href="https://fonts.googleapis.com/css2?family=Arimo:wght@400;700&family=Inter:wght@300&display=swap" rel="stylesheet">
<style>
  :root {
    --canvas: #ffffff;
    --grey-top: #6b6c6f;
    --grey-mid: #8f9094;
    --grey-low: #c9cacc;
    --grey-end: #f1f1f2;
    --yellow: #ffd400;
    --amber: #f7b21a;
    --ink: #1a1a1a;
    --body: #ffffff;
  }
  * { margin: 0; padding: 0; box-sizing: border-box; }
  html, body { width: 1200px; height: 1000px; overflow: hidden; background: var(--canvas); }
  body { position: relative; font-family: "Arimo", Arial, sans-serif; }

  .flyer {
    position: absolute; left: 300px; top: 76px; width: 600px; height: 849px;
    background: linear-gradient(180deg, var(--grey-top) 0%, var(--grey-top) 22%, var(--grey-mid) 55%, var(--grey-low) 80%, var(--grey-end) 100%);
    box-shadow: 2px 3px 5px rgba(0,0,0,0.3);
    overflow: hidden;
  }
  .hero-chevron { position: absolute; left: 94px; top: 118px; width: 108px; height: 112px; }
  .headline {
    position: absolute; left: 222px; top: 113px; width: 262px;
    color: var(--yellow); font-family: "Inter", Arial, sans-serif;
    font-weight: 300; font-size: 24px; line-height: 31px;
  }
  .column { position: absolute; top: 296px; width: 152px; }
  .column--about { left: 57px; }
  .column--benefits { left: 226px; }
  .column--change { left: 394px; }
  .column h2 { color: var(--amber); font-size: 13.5px; font-weight: 700; margin-bottom: 3px; white-space: nowrap; }
  .column ul { list-style: none; }
  .column li {
    color: var(--body); font-size: 12px; line-height: 14.5px; font-weight: 400;
    padding-left: 11px; position: relative; margin-bottom: 3px;
  }
  .column li::before { content: ">"; position: absolute; left: 0; }

  .footer-band { position: absolute; left: 0; top: 669px; width: 600px; height: 180px; }
  .brand {
    position: absolute; left: 408px; top: 782px; display: flex; align-items: center; gap: 9px;
  }
  .brand-mark { width: 24px; height: 24px; background: var(--ink); flex: none; }
  .brand-name { color: var(--ink); font-weight: 700; font-size: 21px; letter-spacing: 0.5px; white-space: nowrap; }
</style>
</head>
<body>
  <main class="flyer">
    <svg class="hero-chevron" viewBox="0 0 108 112" aria-hidden="true">
      <defs>
        <linearGradient id="chevronGold" x1="0" x2="1">
          <stop offset="0" stop-color="#ffe600"/>
          <stop offset="1" stop-color="#f7b21a"/>
        </linearGradient>
      </defs>
      <polygon points="0,0 108,50 108,62 0,112 0,98 86,56 0,14" fill="url(#chevronGold)"/>
    </svg>
    <h1 class="headline">Supplying quality spill management product to the mines in the Hunter Valley and NSW.</h1>

    <section class="column column--about">
      <h2>About Us:</h2>
      <ul>
        <li>Brantoveck is Newcastle’s only owned and operated dedicated Spill Management Company. We currently supply some of the largest mines in NSW, and would like to supply you too.</li>
        <li>We only supply top quality products, to ensure they’ll do the job you need.</li>
      </ul>
    </section>

    <section class="column column--benefits">
      <h2>Benefits of Brantoveck:</h2>
      <ul>
        <li>We manufacture and import products directly, so there is no middle man. This means the best price every time</li>
        <li>We have a large Newcastle warehouse full of stock, meaning its always on hand when you need it</li>
        <li>We’ll deliver to your site</li>
        <li>We can provide a service program, that invludes restocking and usage reports</li>
        <li>We’ve got every spill management product you’ll ever need, we’re you one stop shop</li>
      </ul>
    </section>

    <section class="column column--change">
      <h2>Helping you change:</h2>
      <ul>
        <li>We understand changing products and suppliers in the mining industry can be difficult.</li>
        <li>We’ll assist by:</li>
        <li>Provide samples to conduct onsite testing</li>
        <li>Providing product perforamce details, datsheets and MSDS’s</li>
        <li>Provide onsite training of our products</li>
      </ul>
    </section>

    <svg class="footer-band" viewBox="0 0 600 180">
      <defs>
        <linearGradient id="bandGold" x1="0" x2="1">
          <stop offset="0" stop-color="#ffe600"/>
          <stop offset="1" stop-color="#fbb900"/>
        </linearGradient>
        <linearGradient id="bandBlue" x1="0" x2="1">
          <stop offset="0" stop-color="#0a57a6"/>
          <stop offset="1" stop-color="#0f2b5c"/>
        </linearGradient>
        <linearGradient id="photoTone" x1="0" x2="1" y1="0" y2="1">
          <stop offset="0" stop-color="#c9cdd2"/>
          <stop offset="0.6" stop-color="#b69a86"/>
          <stop offset="1" stop-color="#2f4f86"/>
        </linearGradient>
      </defs>
      <polygon points="0,0 22,0 110,90 22,180 0,180" fill="url(#bandGold)"/>
      <polygon points="0,78 10,90 0,102" fill="#5a3b1e"/>
      <polygon points="48,0 182,0 270,90 182,180 48,180 128,90" fill="url(#photoTone)"
               role="img" aria-label="Photo of a smiling mine worker in hard hat and safety glasses"/>
      <polygon points="196,0 285,0 375,90 285,180 196,180 284,90" fill="url(#bandBlue)"/>
    </svg>

    <div class="brand">
      <span class="brand-mark"></span>
      <span class="brand-name">BRANTOVECK</span>
    </div>
  </main>
</body>
</html>
```